Tending Our Garden eBook Cover Design

I want to deisgn a cover for my eBook (FRONT COVER) and the title is:

What I Grew From a Single Spark. And Why It Matters
By KT Dorran

TITLE CHANGED TO: UNDER THE WILLOW TREE; WHERE I FOUND MY QUIET STRENGTH AND WHERE YOU MIGHT TOO

The color palette is attached. Along with some photos options of me. Along with the ebook in WORD Document. My website is www.KTDorranLive.example. You can use a different color palette if you think it is best

Target Market(s)

women who look to build a personal brand

Industry/Entity Type

health and wellness

Requirements
Must have
• the title
Nice to have
• use my picture on the cover; but that is optional
Should not have
• any men

```html
<!DOCTYPE html>
<html lang="en">
<head>
<meta charset="utf-8">
<title>Under the Willow Tree – eBook Cover</title>
<link rel="stylesheet" href="https://fonts.googleapis.com/css2?family=Montserrat:wght@500;800&family=Lobster&family=Krona+One&family=Yellowtail&display=swap">
<style>
  :root {
    --canvas: #ffffff;
    --pink-light: #f7c1cf;
    --pink-mid: #e6a4b3;
    --rose: #c98493;
    --maroon: #6a2a32;
    --maroon-deep: #56222a;
    --ink: #5a2830;
    --magenta: #d8107a;
    --magenta-shade: #8e0f52;
    --url-pink: #f1a9be;
    --white: #ffffff;
  }
  * { box-sizing: border-box; margin: 0; padding: 0; }
  html, body {
    width: 1200px; height: 1000px; overflow: hidden;
    background: var(--canvas);
  }
  .cover {
    position: absolute;
    left: 278px; top: 44px;
    width: 646px; height: 914px;
    overflow: hidden;
    background:
      radial-gradient(ellipse 300px 260px at 50% 62%, rgba(255,225,232,0.85), rgba(255,225,232,0) 100%),
      linear-gradient(180deg, var(--pink-light) 0%, var(--pink-mid) 45%, var(--rose) 68%, var(--maroon) 90%, var(--maroon-deep) 100%);
  }
  .cover__texture {
    position: absolute; inset: 0;
    background: radial-gradient(ellipse 420px 360px at 50% 30%, rgba(255,255,255,0.12), rgba(255,255,255,0));
  }
  .title {
    position: absolute; left: 0; right: 0; top: 100px;
    text-align: center; color: var(--ink);
    font-weight: normal;
  }
  .title__lead {
    font-family: "Montserrat", sans-serif;
    font-weight: 500; font-size: 42px; line-height: 54px;
  }
  .title__lead strong { font-weight: 800; }
  .title__script {
    font-family: "Lobster", cursive;
    font-size: 58px; line-height: 70px;
  }
  .title__feature {
    font-family: "Krona One", sans-serif;
    font-size: 68px; line-height: 88px;
    color: var(--magenta);
    text-shadow: 3px 3px 0 var(--magenta-shade);
  }
  .title__close {
    font-family: "Montserrat", sans-serif;
    font-weight: 500; font-size: 34px; line-height: 48px; margin-top: 4px;
  }
  .title__close strong { font-weight: 800; }
  .portrait {
    position: absolute; left: 128px; top: 420px;
    width: 392px; height: 494px;
    border-radius: 180px 180px 0 0;
    background: linear-gradient(180deg, rgba(120,50,60,0.55) 0%, rgba(140,70,80,0.6) 40%, rgba(95,36,44,0.85) 75%, var(--maroon-deep) 100%);
  }
  .author {
    position: absolute; left: 0; right: 0; top: 792px;
    text-align: center;
    font-family: "Yellowtail", "Brush Script MT", cursive;
    font-size: 58px; line-height: 70px; color: var(--white);
  }
  .website {
    position: absolute; left: 0; right: 0; top: 882px;
    text-align: center;
    font-family: "Montserrat", sans-serif;
    font-weight: 800; font-size: 13px; color: var(--url-pink);
  }
</style>
</head>
<body>
  <main class="cover">
    <div class="cover__texture" role="img" aria-label="Faint swirling line pattern across the pink background"></div>
    <h1 class="title">
      <div class="title__lead">Under the <strong>Willow Tree;</strong></div>
      <div class="title__script">Where I Found My Quiet</div>
      <div class="title__feature">STRENGTH</div>
      <div class="title__close">And <strong>Where You Might Too</strong></div>
    </h1>
    <div class="portrait" role="img" aria-label="Portrait photograph of the author, tinted in rose tones"></div>
    <p class="author">KT Dorran</p>
    <p class="website">www.KTDorranLive.example</p>
  </main>
</body>
</html>
```